illustrations for fun family trip poster design

I would like a design for a poster featuring myself, my wife, and my dog in illustrative form in front of a beach / palm tree background. I am looking for a Los Angeles / California art deco vibe. If possible, I'd like our heads sticking out the window of the car. If not possible, have cartoonish versions of ourselves.
Please check all the pictures in the brief, as I have included pictures of all of us to help you make us look as accurate as possible. The idea is a concert poster, which has the dates of each stop listed like a concert tour.
Some other detail:
- Can you please make the car navy blue
- Have the dog sticking his head out the sunroof, and the female out the passenger window
- Use the lettering to be block lettering, and use only one color (such as black) and make it closer to the lettering in the "leon harsk poster" image attached
- Can you make time of day to sunset, and include some orange and reds in the skyline

```html
<!DOCTYPE html>
<html lang="en">
<head>
<meta charset="utf-8">
<title>Road Trip 2018</title>
<link rel="stylesheet" href="https://fonts.googleapis.com/css2?family=Bebas+Neue&display=swap">
<style>
  :root {
    --sky-top: #ff5a14;
    --sky-mid: #ff8a2e;
    --sky-low: #ffb765;
    --sun: #ffffff;
    --cloud-peach: #efc09c;
    --cloud-rust: #c8623a;
    --band-red: #a8211c;
    --ink: #1c0606;
    --ink-red: #5e0e0e;
    --dot: #b8553a;
    --suv-navy: #3e4c8a;
    --suv-dark: #27306a;
    --crew-warm: #8c4a32;
  }
  * { margin: 0; padding: 0; box-sizing: border-box; }
  html, body { width: 800px; height: 1200px; overflow: hidden; background: #fff; }
  .poster {
    position: relative;
    width: 800px;
    height: 1200px;
    overflow: hidden;
    font-family: "Bebas Neue", "Oswald", sans-serif;
    background: #fff;
  }
  .backdrop { position: absolute; inset: 0; }
  .title {
    position: absolute;
    top: 92px;
    left: 254px;
    font-size: 76px;
    font-weight: 400;
    line-height: 1;
    color: var(--ink);
    letter-spacing: -1.5px;
    white-space: nowrap;
  }
  .title .year {
    display: inline-block;
    background: #000;
    color: #fff;
    padding: 3px 3px 0;
    margin-left: 8px;
    line-height: 0.8;
    letter-spacing: 0;
  }
  .dates-range {
    position: absolute;
    top: 186px;
    left: 0;
    width: 800px;
    text-align: center;
    padding-left: 0;
    font-size: 29px;
    line-height: 32px;
    letter-spacing: 2.6px;
    color: var(--ink-red);
    white-space: nowrap;
  }
  .tour {
    position: absolute;
    top: 264px;
    list-style: none;
    font-size: 30px;
    letter-spacing: 2.3px;
    line-height: 40px;
    white-space: nowrap;
  }
  .tour-west { right: 448px; text-align: right; color: var(--ink); }
  .tour-south { left: 466px; top: 262px; color: var(--ink-red); }
  .divider {
    position: absolute;
    left: 410px;
    top: 234px;
    width: 6px;
    height: 476px;
    background: radial-gradient(circle, var(--dot) 2.4px, transparent 2.8px) 0 0 / 6px 9.6px repeat-y;
  }
  .travellers { position: absolute; left: 0; top: 0; width: 800px; height: 1200px; }
</style>
</head>
<body>
<main class="poster">
  <svg class="backdrop" width="800" height="1200" viewBox="0 0 800 1200" role="img" aria-label="Sunset beach scene with palm trees and orange and red clouds">
    <defs>
      <linearGradient id="sky" x1="0" y1="0" x2="0" y2="1">
        <stop offset="0" stop-color="var(--sky-top)"/>
        <stop offset="0.55" stop-color="var(--sky-mid)"/>
        <stop offset="1" stop-color="var(--sky-low)"/>
      </linearGradient>
      <linearGradient id="shore" x1="0" y1="0" x2="0" y2="1">
        <stop offset="0" stop-color="var(--cloud-peach)"/>
        <stop offset="0.45" stop-color="var(--cloud-rust)"/>
        <stop offset="1" stop-color="var(--band-red)"/>
      </linearGradient>
    </defs>
    <rect x="0" y="0" width="800" height="360" fill="url(#sky)"/>
    <circle class="sun" cx="560" cy="400" r="384" fill="var(--sun)"/>
    <path d="M0 360 Q120 340 240 372 L240 1200 L0 1200 Z" fill="#fff"/>
    <rect x="0" y="460" width="800" height="740" fill="url(#shore)" opacity="0.55"/>
    <path d="M0 640 Q200 610 420 650 T800 640 L800 720 L0 720 Z" fill="var(--cloud-rust)" opacity="0.45"/>
    <path d="M0 800 Q260 770 520 800 T800 790 L800 1200 L0 1200 Z" fill="var(--band-red)" opacity="0.55"/>
  </svg>

  <h1 class="title">Road Trip<span class="year">2018</span></h1>
  <p class="dates-range">September 17th - November 10th,&nbsp; 2018</p>

  <ul class="tour tour-west">
    <li>Chicago, IL – Sept 17</li>
    <li>Hot Springs, SD – Sept 19</li>
    <li>Bozeman, MT – Sept 21</li>
    <li>Spokane, WA – Sept 24</li>
    <li>Seattle, WA – Sept 25</li>
    <li>Cannon Beach, OR – Sept 28</li>
    <li>Portland, OR – Oct 1</li>
    <li>Mendocino, CA– Oct 5</li>
    <li>Santa Barbara – Oct 8</li>
    <li>Los Angeles, CA – Oct 10</li>
  </ul>

  <div class="divider" aria-hidden="true"></div>

  <ul class="tour tour-south">
    <li>San Diego, CA – Oct 18</li>
    <li>Los Angeles, LA– Oct 21</li>
    <li>Las Vegas – Oct 25</li>
    <li>Grand Canyon– Oct 27</li>
    <li>Sedona, AZ – Oct 29</li>
    <li>Scottsdale, AZ – Oct 31</li>
    <li>El Paso, TX – Nov 2</li>
    <li>Austin, TX – Nov 3</li>
    <li>Nashville, TN – Nov 8</li>
    <li>Detroit – Nov 9</li>
    <li>Toronto – Nov 10</li>
  </ul>

  <svg class="travellers" width="800" height="1200" viewBox="0 0 800 1200" role="img" aria-label="Cartoon of a navy blue SUV with a bearded man at the driver window, a woman in sunglasses at the passenger window and a shaggy brown dog in the sunroof">
    <defs>
      <linearGradient id="crew" x1="0" y1="0" x2="0" y2="1">
        <stop offset="0" stop-color="var(--crew-warm)"/>
        <stop offset="0.42" stop-color="var(--suv-navy)"/>
        <stop offset="1" stop-color="var(--suv-dark)"/>
      </linearGradient>
    </defs>
    <rect x="48" y="712" width="752" height="488" rx="28" fill="url(#crew)"/>
  </svg>
</main>
</body>
</html>
```